Postcard Design

We need a postcard design for our company, Larkmere Business Group. Our firm sources funding (money) solutions for existing small business owners and start-up who are seeking $50,000 to $250,000. We would like to see designs that feature the colors dark or navy blue and gold. (We are uploading our logo for color reference ONLY. We DO NOT want the logo to be a part of the design!) The final design should communicate that we are an established financial source for business owners who are looking for capital to borrow. The final design should also emphasize that we provide quick approval and fast turnaround.
Target Market(s)
Small business owners (less than 10 employees) as well as start-up companies.
Industry/Entity Type
Small Business
Look and feel

```html
<!DOCTYPE html>
<html lang="en">
<head>
<meta charset="utf-8">
<title>Larkmere Business Group Postcard</title>
<link href="https://fonts.googleapis.com/css2?family=Arimo:wght@400;700&display=swap" rel="stylesheet">
<style>
  :root {
    --navy: #1c2a5e;
    --navy-deep: #16214d;
    --gold: #e2b52a;
    --white: #ffffff;
    --sky: #3f7fd0;
    --sky-light: #c9dcf2;
    --paper: #e9eef0;
    --bill: #d4dcd2;
    --page: #f2f2f2;
  }
  html, body {
    margin: 0;
    padding: 0;
    width: 1200px;
    height: 1000px;
    overflow: hidden;
    background: var(--page);
    font-family: "Arimo", Arial, sans-serif;
  }
  .postcard {
    position: absolute;
    left: 50px;
    top: 77px;
    width: 1100px;
    height: 846px;
    background: var(--white);
    overflow: hidden;
    box-shadow: 0 4px 18px rgba(0,0,0,0.18);
  }
  .hero-photo {
    position: absolute;
    left: 0;
    top: 80px;
    width: 1100px;
    height: 682px;
    background: linear-gradient(170deg, var(--sky) 0%, var(--sky-light) 22%, var(--white) 42%, var(--paper) 62%, var(--bill) 100%);
  }
  .header-shape {
    position: absolute;
    left: 0;
    top: 0;
  }
  .brand-name {
    position: absolute;
    left: 40px;
    top: 30px;
    margin: 0;
    font-size: 47px;
    line-height: 50px;
    font-weight: 700;
    color: var(--navy);
    white-space: nowrap;
  }
  .intro-box {
    position: absolute;
    left: 23px;
    top: 143px;
    width: 741px;
    height: 112px;
    padding: 22px;
    margin: 0;
    background: rgba(255,255,255,0.78);
    border: 2px solid rgba(200,210,225,0.9);
    font-size: 26px;
    line-height: 1.5;
    color: var(--navy-deep);
    white-space: nowrap;
  }
  .feature-pill {
    position: absolute;
    left: 23px;
    width: 495px;
    height: 63px;
    background: var(--gold);
    border-radius: 0 32px 32px 0;
    box-shadow: 0 3px 4px rgba(0,0,0,0.25);
    color: var(--navy);
    font-size: 37px;
    font-weight: 700;
    line-height: 63px;
    padding-left: 32px;
    box-sizing: border-box;
  }
  .feature-quick { top: 361px; }
  .feature-fast { top: 470px; }
  .call-label {
    position: absolute;
    left: 38px;
    top: 606px;
    font-size: 30px;
    font-weight: 700;
    color: var(--navy);
  }
  .call-number {
    position: absolute;
    left: 36px;
    top: 646px;
    font-size: 62px;
    font-weight: 700;
    color: var(--navy);
    letter-spacing: 0.5px;
  }
  .footer-rule {
    position: absolute;
    left: 0;
    top: 762px;
    width: 1100px;
    height: 5px;
    background: var(--gold);
  }
  .footer-band {
    position: absolute;
    left: 0;
    top: 770px;
    width: 1100px;
    height: 76px;
    background: var(--navy);
    color: var(--gold);
    font-size: 42px;
    font-weight: 700;
    text-align: center;
    line-height: 76px;
    letter-spacing: 2px;
  }
</style>
</head>
<body>
  <div class="postcard">
    <div class="hero-photo" role="img" aria-label="Photo of a business handshake in front of a blue sky over scattered hundred-dollar bills"></div>

    <svg class="header-shape" width="1100" height="110" viewBox="0 0 1100 110" aria-hidden="true">
      <rect x="0" y="0" width="1100" height="78" fill="var(--navy)"/>
      <rect x="800" y="76" width="300" height="5" fill="var(--white)"/>
      <polygon points="0,0 900,0 810,107 0,107" fill="var(--gold)"/>
    </svg>
    <h1 class="brand-name">LARKMERE BUSINESS GROUP</h1>

    <p class="intro-box">The premier alternative business funding firm, where our<br>customized solutions and business services continue to<br>exceed our clients' expectations.</p>

    <div class="feature-pill feature-quick">QUICK APPROVAL</div>
    <div class="feature-pill feature-fast">FAST TURNAROUND</div>

    <div class="call-label">CALL US TODAY :</div>
    <div class="call-number">0990-482-615</div>

    <div class="footer-rule"></div>
    <div class="footer-band">www.larkmerefunding.com</div>
  </div>
</body>
</html>
```